Brevan Law Business cards and stationary design project

We are looking for a stationary design for business cards (double sided), 8x10, 5x7, and legal and standard envelopes.

We would like the design to match the logo that we have already.
Color palate preferred is Teal, White, grey and any others that will look good for a professional law firm.

We would like this statement: "RELATIONSHIPS. RESPECT. RESULT" to be on the back of the business cards and maybe on the stationary if it looks good.

Please see link to website for more information: www.brevan-law-example.com

Target Market(s)

Potential clients that need Attorney services.

Industry/Entity Type

Law Firm

Contact Information for Business Card

We would like the front and back to be two different colors. Current business cards are teal front, grey back and are a vertical design. We are open to options with colors.

Font styles to use
Serif

Colors
33a6d7
33b8a4
b9b9b9
5c5c5c

Requirements
Must have
• Logo supplied needs to go on the card and stationary.
• Match website color palate, www.brevan-law-example.com
• Be professional and not too wordy.
• Criminal Law, Civil Litigation, Personal Injury, Restraining Orders need to be on the card.
Nice to have
• RELATIONSHIPS. RESPECT. RESULTS. on the back of the card.
Should not have
• Not be too busy/wordy or too flashy.

```html
<!DOCTYPE html>
<html lang="en">
<head>
<meta charset="utf-8">
<title>Brevan Law – Business Cards</title>
<link href="https://fonts.googleapis.com/css2?family=Cinzel:wght@400&family=Open+Sans:wght@400;600&display=swap" rel="stylesheet">
<style>
  :root {
    --teal: #2fb3bd;
    --teal-deep: #138f9c;
    --teal-light: #4cc6cf;
    --white: #ffffff;
    --paper: #f7f8f8;
    --ink: #4a4a4a;
    --backdrop: #e9e7e3;
  }
  * { box-sizing: border-box; margin: 0; padding: 0; }
  html, body { width: 1200px; height: 1023px; overflow: hidden; }
  body { background: var(--backdrop); position: relative; font-family: "Open Sans", sans-serif; }

  .card {
    position: absolute;
    width: 560px;
    height: 320px;
    border-radius: 3px;
    box-shadow: 0 10px 28px rgba(0,0,0,0.18), 0 2px 4px rgba(0,0,0,0.10);
  }

  /* Brand placeholder: plain circle + name in one colour and weight */
  .brand {
    display: flex; flex-direction: column; align-items: center; gap: 14px;
  }
  .brand-mark { width: 58px; height: 58px; border-radius: 50%; background: var(--teal); }
  .brand-name {
    font-family: "Cinzel", serif; font-weight: 400; font-size: 30px; letter-spacing: 2px;
    color: var(--teal); white-space: nowrap;
  }

  /* Front */
  .card-front { left: 90px; top: 110px; background: linear-gradient(160deg, var(--white), var(--paper)); }
  .front-brand {
    position: absolute; left: 0; top: 30px; width: 270px; height: 200px;
    justify-content: center;
  }
  .front-divider { position: absolute; left: 270px; top: 40px; width: 1px; height: 170px; background: var(--teal); }
  .contact { position: absolute; left: 296px; top: 48px; color: var(--ink); font-size: 12px; line-height: 1.6; }
  .contact-name { font-family: "Cinzel", serif; font-size: 22px; color: var(--teal); letter-spacing: 1px; line-height: 1.1; }
  .contact-title { font-size: 10px; letter-spacing: 1px; text-transform: uppercase; color: var(--ink); margin-bottom: 12px; }
  .contact-line .tag { color: var(--teal); font-weight: 600; margin-right: 6px; }
  .contact-address { margin-top: 10px; }
  .practice-areas {
    position: absolute; left: 0; right: 0; bottom: 26px; text-align: center;
    font-size: 11.5px; color: var(--ink);
  }
  .practice-areas .dot {
    display: inline-block; width: 6px; height: 6px; border-radius: 50%; background: var(--teal);
    margin: 0 6px; vertical-align: middle;
  }

  /* Back */
  .card-back {
    left: 550px; top: 590px;
    background: radial-gradient(ellipse at 70% 40%, var(--teal-light), var(--teal) 45%, var(--teal-deep));
    display: flex; flex-direction: column; align-items: center; justify-content: center;
  }
  .card-back .brand-mark { background: var(--white); width: 64px; height: 64px; }
  .card-back .brand-name { color: var(--white); font-size: 34px; }
  .tagline {
    margin-top: 34px; font-family: "Cinzel", serif; font-size: 17px; letter-spacing: 3px; color: var(--white);
  }
</style>
</head>
<body>
  <section class="card card-front">
    <div class="brand front-brand">
      <span class="brand-mark"></span>
      <span class="brand-name">Brevan Law</span>
    </div>
    <div class="front-divider"></div>
    <div class="contact">
      <div class="contact-name">Dana Mercer</div>
      <div class="contact-title">Lawyer</div>
      <div class="contact-line"><span class="tag">[P]</span>(555) 014-2298</div>
      <div class="contact-line"><span class="tag">[E]</span>dana@brevan-law-example.com</div>
      <div class="contact-line"><span class="tag">[W]</span>www.brevan-law-example.com</div>
      <div class="contact-address">418 Harbor View Ave. #200<br>Coastline City, CA 90000</div>
    </div>
    <p class="practice-areas">Practice areas<span class="dot"></span>Criminal Law<span class="dot"></span>Civil Litigation/Personal Injury<span class="dot"></span>Restraining Orders</p>
  </section>

  <section class="card card-back">
    <div class="brand">
      <span class="brand-mark"></span>
      <span class="brand-name">Brevan Law</span>
    </div>
    <p class="tagline">RELATIONSHIPS. RESPECT. RESULTS.</p>
  </section>
</body>
</html>
```